Estate Planning Law Firm opening new branch in Florida

I am an experienced estate planning attorney that recently relocated to Florida. Looking for a banner Ad to place on platforms such as YardLoop, Chatterly and Pixmora to create publicity for firm and new leads.

```html
<!DOCTYPE html>
<html lang="en">
<head>
<meta charset="utf-8">
<title>Serenova Law Firm – Banner Ads</title>
<link rel="stylesheet" href="https://fonts.googleapis.com/css2?family=Poppins:wght@400;600;700&family=Cinzel:wght@400;600;700&family=Allura&display=swap">
<style>
  :root{
    --teal:#1e6f6d;
    --teal-light:#3a8582;
    --navy:#2b3a4e;
    --grey:#b4b4b4;
    --board:#b5b5b5;
    --white:#ffffff;
  }
  *{margin:0;padding:0;box-sizing:border-box}
  html,body{width:848px;height:1200px;overflow:hidden;background:var(--board)}
  .board{position:relative;width:848px;height:1200px}

  .banner{position:absolute;background:var(--white);overflow:hidden;box-shadow:6px 8px 10px rgba(0,0,0,.25)}
  .banner--wide{left:51px;top:69px;width:751px;height:393px}
  .banner--square{left:114px;top:504px;width:625px;height:625px}

  .banner__art,.banner__photo{position:absolute;left:0;top:0;width:100%;height:100%}

  .brand{position:absolute;display:flex;align-items:center;gap:8px;color:var(--navy)}
  .brand__mark{background:var(--teal)}
  .brand__text{display:flex;flex-direction:column;align-items:center}
  .brand__name{font-family:"Cinzel",serif;font-weight:700;line-height:1;letter-spacing:.5px}
  .brand__sub{font-family:"Poppins",sans-serif;font-weight:400;display:flex;align-items:center;gap:5px;line-height:1.2}
  .brand__sub::before,.brand__sub::after{content:"";display:block;height:1px;background:var(--teal)}

  .headline{position:absolute;font-family:"Poppins",sans-serif;font-weight:700;color:var(--teal);line-height:1.02;letter-spacing:-.2px}
  .tagline{position:absolute;font-family:"Cinzel",serif;font-weight:400;color:var(--navy);line-height:1.15;text-transform:uppercase}

  .advisor{position:absolute;display:flex;flex-direction:column;align-items:flex-end}
  .advisor__name{font-family:"Allura",cursive;color:var(--navy);line-height:1;white-space:nowrap}
  .advisor__role{font-family:"Poppins",sans-serif;font-weight:600;color:var(--teal);line-height:1;white-space:nowrap}

  .call{position:absolute;display:flex;align-items:center}
  .call__icon{display:block}
  .call__label{font-family:"Cinzel",serif;font-weight:400;color:var(--navy);line-height:1}
  .call__number{font-family:"Poppins",sans-serif;font-weight:700;color:var(--teal);line-height:1.1}

  .contact{position:absolute;display:flex;align-items:center;font-family:"Poppins",sans-serif;font-weight:400;color:var(--navy);white-space:nowrap}

  /* wide banner */
  .banner--wide .brand{left:43px;top:48px}
  .banner--wide .brand__mark{width:26px;height:26px}
  .banner--wide .brand__name{font-size:31px}
  .banner--wide .brand__sub{font-size:10px}
  .banner--wide .brand__sub::before,.banner--wide .brand__sub::after{width:36px}
  .banner--wide .headline{left:43px;top:138px;font-size:30px}
  .banner--wide .tagline{left:43px;top:210px;font-size:10.5px;width:430px}
  .banner--wide .advisor{right:251px;top:246px}
  .banner--wide .advisor__name{font-size:30px}
  .banner--wide .advisor__role{font-size:9.5px;margin-top:-2px}
  .banner--wide .call{left:43px;top:306px;gap:8px}
  .banner--wide .call__label{font-size:11px}
  .banner--wide .call__number{font-size:21px}
  .banner--wide .contact{font-size:9.5px;top:364px;gap:6px}
  .banner--wide .contact--web{left:202px}
  .banner--wide .contact--mail{left:409px}

  /* square banner */
  .banner--square .brand{left:32px;top:58px}
  .banner--square .brand__mark{width:32px;height:32px}
  .banner--square .brand__name{font-size:38px}
  .banner--square .brand__sub{font-size:12.5px}
  .banner--square .brand__sub::before,.banner--square .brand__sub::after{width:44px}
  .banner--square .headline{left:28px;top:160px;font-size:35px;width:330px}
  .banner--square .tagline{left:28px;top:280px;font-size:12px;width:330px}
  .banner--square .advisor{right:326px;top:370px}
  .banner--square .advisor__name{font-size:36px}
  .banner--square .advisor__role{font-size:12px;margin-top:-2px}
  .banner--square .call{left:28px;top:478px;gap:11px}
  .banner--square .call__label{font-size:13.5px}
  .banner--square .call__number{font-size:28px}
  .banner--square .contact{font-size:13px;top:573px;gap:7px}
  .banner--square .contact--web{left:75px}
  .banner--square .contact--mail{left:353px}
</style>
</head>
<body>
<main class="board">

  <!-- Wide banner -->
  <section class="banner banner--wide">
    <svg class="banner__art" viewBox="0 0 751 393" aria-hidden="true">
      <line x1="571" y1="420" x2="733" y2="258" stroke="var(--grey)" stroke-width="80" stroke-linecap="round"/>
      <line x1="686" y1="12" x2="720" y2="-22" stroke="var(--grey)" stroke-width="26" stroke-linecap="round"/>
    </svg>
    <svg class="banner__photo" viewBox="0 0 751 393" role="img" aria-label="Portrait photo of the financial planner in a navy suit against an office backdrop">
      <defs>
        <linearGradient id="photoWide" x1="0" y1="0" x2="0" y2="1">
          <stop offset="0" stop-color="var(--teal-light)"/>
          <stop offset=".55" stop-color="var(--teal)"/>
          <stop offset="1" stop-color="var(--navy)"/>
        </linearGradient>
      </defs>
      <circle cx="634" cy="231" r="120" fill="url(#photoWide)"/>
      <polygon points="549,146 849,-154 1019,16 719,316" fill="url(#photoWide)"/>
      <line x1="735" y1="126" x2="800" y2="61" stroke="var(--white)" stroke-width="34" stroke-linecap="round"/>
    </svg>

    <div class="brand">
      <span class="brand__mark"></span>
      <div class="brand__text">
        <span class="brand__name">SERENOVA</span>
        <span class="brand__sub">LAW FIRM, PLLC</span>
      </div>
    </div>

    <h1 class="headline">Are you ready to take<br>control of your future?</h1>
    <p class="tagline">We are Serenova, Florida's premier estate planning and financial planning two-in-one firm</p>

    <div class="advisor">
      <p class="advisor__name">Daniel Whitcombe</p>
      <p class="advisor__role">FINANCIAL PLANNER</p>
    </div>

    <div class="call">
      <svg class="call__icon" width="31" height="33" viewBox="0 0 31 33" aria-hidden="true">
        <rect x="3" y="0" width="28" height="33" rx="2" fill="var(--teal)"/>
        <g fill="var(--teal)"><rect x="0" y="5" width="5" height="2" rx="1"/><rect x="0" y="11" width="5" height="2" rx="1"/><rect x="0" y="17" width="5" height="2" rx="1"/><rect x="0" y="23" width="5" height="2" rx="1"/></g>
        <path d="M11 10c1-1 2-1 2.5 0l1 2c.3.7 0 1.2-.6 1.5-.5.3-.4 1.2.3 2.7.7 1.5 1.5 2.2 2 2 .6-.3 1.2-.3 1.6.3l1.1 1.8c.4.8 0 1.5-1 2-2.5 1.2-5.5-1.5-7-5s-1.4-6 .1-7.3z" fill="var(--white)"/>
        <path d="M21 13a4 4 0 0 1 0 6M24 11a7 7 0 0 1 0 10" stroke="var(--white)" stroke-width="1.3" fill="none" stroke-linecap="round"/>
      </svg>
      <div>
        <p class="call__label">Book an Initial Call</p>
        <p class="call__number">(321) 555-0148</p>
      </div>
    </div>

    <p class="contact contact--web">
      <svg width="17" height="17" viewBox="0 0 20 20" aria-hidden="true"><g fill="none" stroke="var(--navy)" stroke-width="1.6"><circle cx="10" cy="10" r="8.5"/><ellipse cx="10" cy="10" rx="3.8" ry="8.5"/><line x1="1.5" y1="10" x2="18.5" y2="10"/><line x1="3" y1="5.5" x2="17" y2="5.5"/><line x1="3" y1="14.5" x2="17" y2="14.5"/></g></svg>
      KEEPANDBUILDWEALTH.COM
    </p>
    <p class="contact contact--mail">
      <svg width="16" height="11" viewBox="0 0 20 14" aria-hidden="true"><rect width="20" height="14" fill="var(--navy)"/><path d="M1 1l9 7 9-7" stroke="var(--white)" stroke-width="1.6" fill="none"/></svg>
      HELLO@SERENOVA.LAW
    </p>
  </section>

  <!-- Square banner -->
  <section class="banner banner--square">
    <svg class="banner__art" viewBox="0 0 625 625" aria-hidden="true">
      <line x1="356" y1="680" x2="591" y2="475" stroke="var(--grey)" stroke-width="100" stroke-linecap="round"/>
      <line x1="539" y1="84" x2="650" y2="-27" stroke="var(--grey)" stroke-width="34" stroke-linecap="round"/>
    </svg>
    <svg class="banner__photo" viewBox="0 0 625 625" role="img" aria-label="Portrait photo of the financial planner in a navy suit against an office backdrop">
      <defs>
        <linearGradient id="photoSquare" x1="0" y1="0" x2="0" y2="1">
          <stop offset="0" stop-color="var(--teal-light)"/>
          <stop offset=".55" stop-color="var(--teal)"/>
          <stop offset="1" stop-color="var(--navy)"/>
        </linearGradient>
      </defs>
      <circle cx="473" cy="373" r="165" fill="url(#photoSquare)"/>
      <polygon points="356,256 756,-144 990,90 590,490" fill="url(#photoSquare)"/>
      <line x1="590" y1="232" x2="680" y2="142" stroke="var(--white)" stroke-width="46" stroke-linecap="round"/>
    </svg>

    <div class="brand">
      <span class="brand__mark"></span>
      <div class="brand__text">
        <span class="brand__name">SERENOVA</span>
        <span class="brand__sub">LAW FIRM, PLLC</span>
      </div>
    </div>

    <h2 class="headline">Are you ready to take control of your future?</h2>
    <p class="tagline">We are Serenova, Florida's premier estate planning and financial planning two-in-one firm</p>

    <div class="advisor">
      <p class="advisor__name">Daniel Whitcombe</p>
      <p class="advisor__role">FINANCIAL PLANNER</p>
    </div>

    <div class="call">
      <svg class="call__icon" width="40" height="44" viewBox="0 0 31 33" aria-hidden="true">
        <rect x="3" y="0" width="28" height="33" rx="2" fill="var(--teal)"/>
        <g fill="var(--teal)"><rect x="0" y="5" width="5" height="2" rx="1"/><rect x="0" y="11" width="5" height="2" rx="1"/><rect x="0" y="17" width="5" height="2" rx="1"/><rect x="0" y="23" width="5" height="2" rx="1"/></g>
        <path d="M11 10c1-1 2-1 2.5 0l1 2c.3.7 0 1.2-.6 1.5-.5.3-.4 1.2.3 2.7.7 1.5 1.5 2.2 2 2 .6-.3 1.2-.3 1.6.3l1.1 1.8c.4.8 0 1.5-1 2-2.5 1.2-5.5-1.5-7-5s-1.4-6 .1-7.3z" fill="var(--white)"/>
        <path d="M21 13a4 4 0 0 1 0 6M24 11a7 7 0 0 1 0 10" stroke="var(--white)" stroke-width="1.3" fill="none" stroke-linecap="round"/>
      </svg>
      <div>
        <p class="call__label">Book an Initial Call</p>
        <p class="call__number">(321) 555-0148</p>
      </div>
    </div>

    <p class="contact contact--web">
      <svg width="23" height="23" viewBox="0 0 20 20" aria-hidden="true"><g fill="none" stroke="var(--navy)" stroke-width="1.6"><circle cx="10" cy="10" r="8.5"/><ellipse cx="10" cy="10" rx="3.8" ry="8.5"/><line x1="1.5" y1="10" x2="18.5" y2="10"/><line x1="3" y1="5.5" x2="17" y2="5.5"/><line x1="3" y1="14.5" x2="17" y2="14.5"/></g></svg>
      KEEPANDBUILDWEALTH.COM
    </p>
    <p class="contact contact--mail">
      <svg width="21" height="14" viewBox="0 0 20 14" aria-hidden="true"><rect width="20" height="14" fill="var(--navy)"/><path d="M1 1l9 7 9-7" stroke="var(--white)" stroke-width="1.6" fill="none"/></svg>
      HELLO@SERENOVA.LAW
    </p>
  </section>

</main>
</body>
</html>
```